business card design for luxurious real estate brand

using the attached logo, i am looking for a 2-sided business card design. the back should be the gold logo on black background. the front needs to include: gold logo, name, phone, email, and website

Industry/Entity Type

real estate

Contact Information for Business Card

logo, name, email, phone, website

Font styles to use
Sans Serif

```html
<!DOCTYPE html>
<html lang="en">
<head>
<meta charset="utf-8">
<title>Casa Verona — Business Card</title>
<link rel="stylesheet" href="https://fonts.googleapis.com/css2?family=Montserrat:wght@300;400;600;700&display=swap">
<style>
  :root {
    --page-bg: #1e1e1f;
    --card-top: #454346;
    --card-bottom: #2b2a2c;
    --gold: #f2cf1d;
    --text-light: #d9d8da;
    --pattern-a: #4a494c;
    --pattern-b: #2f2e30;
  }
  * { box-sizing: border-box; margin: 0; padding: 0; }
  html, body { width: 1200px; height: 1200px; overflow: hidden; }
  body {
    background: var(--page-bg);
    font-family: "Montserrat", sans-serif;
    display: flex;
    flex-direction: column;
    align-items: center;
    justify-content: center;
    gap: 60px;
  }
  .card {
    position: relative;
    width: 880px;
    height: 503px;
    background: linear-gradient(160deg, var(--card-top), var(--card-bottom));
    box-shadow: 0 18px 40px rgba(0,0,0,0.45);
    overflow: hidden;
  }

  /* Front */
  .brand {
    position: absolute;
    left: 190px;
    top: 80px;
    display: flex;
    align-items: center;
    gap: 14px;
    color: var(--gold);
    font-weight: 600;
    font-size: 34px;
    letter-spacing: 6px;
    text-transform: uppercase;
  }
  .brand-square {
    width: 26px;
    height: 26px;
    background: var(--gold);
  }
  .divider {
    position: absolute;
    left: 150px;
    right: 150px;
    top: 272px;
    height: 2px;
    background: var(--gold);
  }
  .person {
    position: absolute;
    right: 150px;
    top: 178px;
    text-align: right;
  }
  .person-name {
    color: var(--gold);
    font-weight: 700;
    font-size: 40px;
    line-height: 1.1;
  }
  .person-title {
    color: var(--text-light);
    font-weight: 300;
    font-size: 22px;
    margin-top: 6px;
  }
  .contacts {
    position: absolute;
    left: 150px;
    top: 300px;
    list-style: none;
    color: var(--text-light);
    font-weight: 400;
    font-size: 20px;
  }
  .contacts li {
    display: flex;
    align-items: center;
    gap: 12px;
    line-height: 36px;
  }
  .contacts svg { width: 18px; height: 18px; flex: none; }

  /* Back */
  .back-pattern {
    position: absolute;
    inset: 0;
    background: repeating-linear-gradient(0deg, var(--pattern-a) 0 30px, var(--pattern-b) 30px 95px);
  }
  .back-brand {
    position: absolute;
    inset: 0;
    display: flex;
    align-items: center;
    justify-content: center;
    color: var(--gold);
    font-weight: 600;
    font-size: 40px;
    letter-spacing: 8px;
    text-transform: uppercase;
  }
  .back-brand span {
    background: var(--card-bottom);
    padding: 12px 28px;
  }
</style>
</head>
<body>
  <section class="card card-front">
    <div class="brand"><span class="brand-square"></span>Casa Verona</div>
    <div class="person">
      <div class="person-name">Dorian Vale</div>
      <div class="person-title">Founder &amp; Director</div>
    </div>
    <div class="divider"></div>
    <ul class="contacts">
      <li>
        <svg viewBox="0 0 24 24" fill="var(--gold)"><path d="M6.6 10.8a15.1 15.1 0 0 0 6.6 6.6l2.2-2.2a1 1 0 0 1 1-.25 11.4 11.4 0 0 0 3.6.57 1 1 0 0 1 1 1V20a1 1 0 0 1-1 1A17 17 0 0 1 3 4a1 1 0 0 1 1-1h3.5a1 1 0 0 1 1 1c0 1.25.2 2.45.57 3.6a1 1 0 0 1-.25 1z"/></svg>
        (405)-555-0147
      </li>
      <li>
        <svg viewBox="0 0 24 24" fill="var(--gold)"><path d="M2 5h20v14H2z"/><path d="M2 5l10 8 10-8" fill="none" stroke="#2b2a2c" stroke-width="2"/></svg>
        dorian@casaverona.com
      </li>
      <li>
        <svg viewBox="0 0 24 24" fill="none" stroke="var(--gold)" stroke-width="2"><circle cx="12" cy="12" r="10" fill="var(--gold)" stroke="none"/><path d="M2 12h20M12 2c3 3 3 17 0 20M12 2c-3 3-3 17 0 20" stroke="#2b2a2c" stroke-width="1.5"/></svg>
        www.casaverona.com
      </li>
    </ul>
  </section>

  <section class="card card-back">
    <div class="back-pattern" role="img" aria-label="Embossed repeating brand-mark pattern in tonal greys"></div>
    <div class="back-brand"><span>Casa Verona</span></div>
  </section>
</body>
</html>
```